Premium label design for product needed

UPDATE: (Scroll down)
For a face care product i need a new front label on the bottle. The current one is white and i want to add the franchise color green. The objective is to premiunize the packaging and to give guidance to the consumers to find their franchise color. The task is to find several option to color the label on the bottle in the most premium way. But at the same time it should not be playful, more in a serious medical direction or in a counterbrand direction. It should look absolutely premium. but should not shout to much. The text structure should remain the same. I will provide a powerpoint slide to illustrate the task even clearer.
UPDATE: DO NOT DESIGN THE FOLDING BOX, only design the bottle. The folding box only serves the purpose of giving the text/layout structure and rough color intent.

Target Market(s)

female 25-39

Requirements
Must have
• Premium, Uniqueness, Innovative

```html
<!DOCTYPE html>
<html lang="en">
<head>
<meta charset="utf-8">
<title>Neo Skin Therapy – B.X. Matt Fluid Label</title>
<link href="https://fonts.googleapis.com/css2?family=Open+Sans:wght@300;400;600;700&display=swap" rel="stylesheet">
<style>
  :root {
    --label-bg: #fdfdfd;
    --frame: #8c8c8c;
    --ink: #0b0b0b;
    --green-deep: #2f8a2a;
    --green-mid: #5fa51f;
    --green-lime: #97c61a;
  }
  html, body {
    margin: 0;
    padding: 0;
    width: 1200px;
    height: 4062px;
    overflow: hidden;
    background: var(--label-bg);
  }
  .label {
    position: relative;
    width: 1200px;
    height: 4062px;
    background: var(--label-bg);
    font-family: "Open Sans", sans-serif;
    color: var(--ink);
  }
  .label__frame {
    position: absolute;
    left: 4px;
    top: 4px;
    width: 1180px;
    height: 4034px;
    border: 6px solid var(--frame);
  }
  .label__text {
    position: absolute;
    left: 0;
    width: 1200px;
    margin: 0;
    text-align: center;
    line-height: 1;
    white-space: nowrap;
  }
  .brand-line--primary {
    top: 2710px;
    font-size: 172px;
    font-weight: 700;
    letter-spacing: 2px;
  }
  .brand-line--secondary {
    top: 2858px;
    font-size: 172px;
    font-weight: 400;
    letter-spacing: 6px;
  }
  .franchise-bar {
    position: absolute;
    left: 177px;
    top: 3118px;
    width: 842px;
    height: 36px;
    background: linear-gradient(90deg, var(--green-mid) 0%, var(--green-deep) 13%, var(--green-mid) 40%, var(--green-lime) 75%, var(--green-lime) 100%);
  }
  .product-name {
    top: 3282px;
    font-size: 96px;
    font-weight: 700;
  }
  .category {
    top: 3804px;
    font-size: 70px;
    font-weight: 600;
    letter-spacing: 2px;
  }
</style>
</head>
<body>
  <main class="label">
    <div class="label__frame"></div>
    <h1 class="label__text brand-line--primary">NEO SKIN</h1>
    <p class="label__text brand-line--secondary">THERAPY</p>
    <div class="franchise-bar"></div>
    <p class="label__text product-name">B.X. MATT FLUID</p>
    <p class="label__text category">DERMITOLIGICAL SKINCARE</p>
  </main>
</body>
</html>
```